High-end residential home builder needs a business card design

We need a new business card design for a small residential construction company based in Boise, Idaho. We specialize in building custom high-end homes and remodels, with a focus on great design and craftsmanship.

We would like to use our current logo, but open to new color suggestions.
Just looking for a clean, sharp, modern design that looks high-end.

Target Market(s)

Upscale clientele

Industry/Entity Type

Contractor

Contact Information for Business Card

Company: Stonefield Custom Builders
Name: Marcus Tilley
Phone number: 208 367 4120
Email: MarcusTilleySCB@mailbox-example.com
Website: Stonefieldcustombuilders-example.com

Font styles to use
Serif
Sans Serif

Requirements
Must have
• Company Logo
Company name
My name
My phone number
My email
Company website
Nice to have
• I have attached a few photos of cards that I really like.

```html
<!DOCTYPE html>
<html lang="en">
<head>
<meta charset="utf-8">
<title>Stonefield Custom Builders – Business Card</title>
<link rel="stylesheet" href="https://fonts.googleapis.com/css2?family=Raleway:wght@500;600;700&family=Open+Sans:wght@400&display=swap">
<style>
  :root {
    --backdrop: #ababab;
    --espresso: #331d0c;
    --amber: #e08d29;
    --paper: #ffffff;
    --shadow: rgba(0, 0, 0, 0.55);
  }
  * { box-sizing: border-box; margin: 0; padding: 0; }
  html, body {
    width: 1200px;
    height: 801px;
    overflow: hidden;
    background: var(--backdrop);
  }
  .stage { position: relative; width: 1200px; height: 801px; }
  .card {
    position: absolute;
    top: 274px;
    width: 443px;
    height: 263px;
    box-shadow: 2px 2px 1px var(--shadow);
    overflow: hidden;
  }
  /* Front: contact side */
  .card-front { left: 153px; background: var(--espresso); }
  .accent-strip {
    position: absolute;
    top: 0; right: 0;
    width: 88px; height: 100%;
    background: var(--amber);
  }
  .holder-name {
    position: absolute;
    left: 25px; top: 154px;
    font-family: "Raleway", sans-serif;
    font-weight: 700;
    font-size: 16.5px;
    color: var(--amber);
  }
  .contact-list {
    position: absolute;
    left: 25px; top: 191px;
    list-style: none;
    font-family: "Open Sans", sans-serif;
    font-size: 11.5px;
    color: var(--paper);
  }
  .contact-list li {
    display: flex;
    align-items: center;
    height: 15.6px;
  }
  .contact-icon { width: 12px; height: 12px; margin-right: 5px; flex: none; }
  /* Back: brand side */
  .card-back { left: 625px; background: var(--paper); }
  .brand {
    position: absolute;
    left: 86px; top: 76px;
    display: flex;
    align-items: center;
    gap: 17px;
  }
  .brand-dot {
    width: 70px; height: 70px;
    border-radius: 50%;
    background: var(--espresso);
    flex: none;
  }
  .brand-name {
    font-family: "Raleway", sans-serif;
    font-weight: 600;
    font-size: 13px;
    line-height: 1.9;
    letter-spacing: 0.34em;
    color: var(--espresso);
  }
  .tagline-band {
    position: absolute;
    left: 0; top: 195px;
    width: 100%; height: 43px;
    background: var(--espresso);
    display: flex;
    align-items: center;
    justify-content: center;
  }
  .tagline {
    font-family: "Raleway", sans-serif;
    font-weight: 600;
    font-size: 16px;
    letter-spacing: 0.16em;
    color: var(--amber);
  }
</style>
</head>
<body>
<main class="stage">
  <section class="card card-front">
    <div class="accent-strip"></div>
    <h1 class="holder-name">MARCUS TILLEY</h1>
    <ul class="contact-list">
      <li>
        <svg class="contact-icon" viewBox="0 0 24 24" aria-hidden="true"><path fill="var(--amber)" d="M6.6 10.8a15 15 0 0 0 6.6 6.6l2.2-2.2a1 1 0 0 1 1-.25 11.4 11.4 0 0 0 3.6.57 1 1 0 0 1 1 1V20a1 1 0 0 1-1 1A17 17 0 0 1 3 4a1 1 0 0 1 1-1h3.5a1 1 0 0 1 1 1c0 1.25.2 2.45.57 3.57a1 1 0 0 1-.25 1z"/></svg>
        208 367 4120
      </li>
      <li>
        <svg class="contact-icon" viewBox="0 0 24 24" aria-hidden="true"><rect x="2" y="5" width="20" height="14" fill="var(--amber)"/><path d="M2 5l10 8 10-8" fill="none" stroke="var(--espresso)" stroke-width="1.6"/></svg>
        MarcusTilleySCB@mailbox-example.com
      </li>
      <li>
        <svg class="contact-icon" viewBox="0 0 24 24" aria-hidden="true"><g fill="none" stroke="var(--amber)" stroke-width="2"><circle cx="12" cy="12" r="9"/><ellipse cx="12" cy="12" rx="4" ry="9"/><path d="M3 12h18M5 7h14M5 17h14"/></g></svg>
        www.Stonefieldcustombuilders-example.com
      </li>
    </ul>
  </section>

  <section class="card card-back">
    <div class="brand">
      <div class="brand-dot"></div>
      <p class="brand-name">STONEFIELD<br>CUSTOM BUILDERS</p>
    </div>
    <div class="tagline-band">
      <p class="tagline">PRECISION MADE TO LAST</p>
    </div>
  </section>
</main>
</body>
</html>
```